2 Wine Label Designs

Amberly Cellars has been helping people give customized wine gifts since 1999. From large scale corporate clients, to 1 bottle personalized gifts, we offer a wide range of wines and templates for any occasion. Recently we’ve started to shift our focus to a younger demographic (21 to 35 year old women) and are in the process of updating our website and branding.

One big area we’re working to improve is the customizable wine label/engraving templates we offer on the site (to see our current template library go to www.amberlycellars.com/shop/wine, select a wine, choose “label” or “engraving” from the dropdown, and click “customize”). You’ll find that a lot of our current templates are outdated or aimed at an older demographic. Over the next few months we want to swap out most of these old templates with fun fresh designs.

We're asking designers to submit 2 customizable wine label templates for this project. One should be wedding themed and the other "Thank You" themed. Please see the attached PDF for more guidelines and creative direction.

Keep in mind, even if you aren't selected as the winner of this project we are going to go through and offer $50 for any label template submitted that we like ($100 if we want both). So there is a good chance you'll be getting some money for your work!

Please read though the attached guidelines PDF carefully (especially the "Must be Customizable" section).

Target Market(s)

21 to 35 year old women

Colors

Designer to choose colors to be used in the design.

Requirements
Must have
• See attached PDF
Nice to have
• See attached PDF
Should not have
• See attached PDF

```html
<!DOCTYPE html>
<html lang="en">
<head>
<meta charset="utf-8">
<title>Wedding label preview</title>
<link rel="stylesheet" href="https://fonts.googleapis.com/css2?family=Nothing+You+Could+Do&family=Open+Sans:wght@400&display=swap">
<style>
  :root {
    --page: #ffffff;
    --label: #ffffff;
    --ink-red: #c41a2b;
    --ink-dark: #111111;
    --caption: #111111;
    --shadow: rgba(0, 0, 0, 0.55);
    --petal: rgba(217, 38, 44, 0.85);
    --leaf: rgba(47, 138, 134, 0.38);
    --leaf-light: rgba(143, 191, 74, 0.25);
  }
  * { margin: 0; padding: 0; box-sizing: border-box; }
  html, body {
    width: 1200px;
    height: 1000px;
    overflow: hidden;
    background: var(--page);
  }
  .canvas {
    position: relative;
    width: 1200px;
    height: 1000px;
    background: var(--page);
  }
  .preview-caption {
    position: absolute;
    left: 42px;
    top: 124px;
    font-family: "Open Sans", sans-serif;
    font-size: 20px;
    line-height: 1.25;
    color: var(--caption);
  }
  .label {
    position: absolute;
    left: 327px;
    top: 110px;
    width: 628px;
    height: 807px;
    background: var(--label);
    box-shadow: 6px 8px 7px var(--shadow);
  }
  .floral {
    position: absolute;
    inset: 0;
  }
  .blob {
    position: absolute;
    display: block;
  }
  .blob--flower {
    background: radial-gradient(ellipse closest-side, var(--petal) 0 55%, rgba(217,38,44,0) 100%);
  }
  .blob--leaves {
    background: radial-gradient(ellipse closest-side, var(--leaf) 0 35%, var(--leaf-light) 70%, rgba(143,191,74,0) 100%);
  }
  /* top-left spray */
  .tl-leaves-right { left: 130px; top: 40px;  width: 210px; height: 110px; }
  .tl-leaves-down  { left: 15px;  top: 140px; width: 160px; height: 190px; }
  .tl-flower       { left: 45px;  top: 45px;  width: 140px; height: 135px; }
  /* top-right sprig */
  .tr-leaves       { left: 495px; top: 38px;  width: 100px; height: 105px; }
  .tr-flower       { left: 545px; top: 42px;  width: 50px;  height: 48px; }
  /* bottom-right spray */
  .br-leaves-up    { left: 455px; top: 490px; width: 150px; height: 210px; }
  .br-leaves-left  { left: 285px; top: 660px; width: 200px; height: 120px; }
  .br-flower       { left: 445px; top: 635px; width: 140px; height: 135px; }

  .script {
    position: absolute;
    font-family: "Nothing You Could Do", cursive;
    color: var(--ink-red);
    white-space: nowrap;
    line-height: 1;
  }
  .couple-name--first { left: 212px; top: 178px; font-size: 78px; }
  .couple-name--second { left: 232px; top: 262px; font-size: 78px; }
  .divider {
    position: absolute;
    left: 120px;
    top: 363px;
    width: 322px;
    height: 24px;
  }
  .wish--line1 { left: 100px; top: 405px; font-size: 100px; }
  .wish--line2 { left: 110px; top: 498px; font-size: 100px; }
  .wedding-date {
    position: absolute;
    left: 55px;
    top: 710px;
    font-family: "Nothing You Could Do", cursive;
    font-size: 36px;
    color: var(--ink-dark);
    line-height: 1;
  }
</style>
</head>
<body>
<div class="canvas">
  <p class="preview-caption">Wedding label<br>preview</p>

  <section class="label">
    <div class="floral floral--top-left" role="img" aria-label="Painted red poppy with teal leafy sprigs">
      <span class="blob blob--leaves tl-leaves-right"></span>
      <span class="blob blob--leaves tl-leaves-down"></span>
      <span class="blob blob--flower tl-flower"></span>
    </div>
    <div class="floral floral--top-right" role="img" aria-label="Small painted red poppy with leaves">
      <span class="blob blob--leaves tr-leaves"></span>
      <span class="blob blob--flower tr-flower"></span>
    </div>
    <div class="floral floral--bottom-right" role="img" aria-label="Painted red poppy with teal leafy branches">
      <span class="blob blob--leaves br-leaves-up"></span>
      <span class="blob blob--leaves br-leaves-left"></span>
      <span class="blob blob--flower br-flower"></span>
    </div>

    <p class="script couple-name couple-name--first">Daniel</p>
    <p class="script couple-name couple-name--second">+ Helena</p>

    <svg class="divider" viewBox="0 0 322 24" aria-hidden="true">
      <path d="M2 6 Q160 1 320 4 Q160 8 2 8 Z" fill="var(--ink-red)"/>
      <path d="M4 17 Q160 13 316 15 Q160 20 4 19 Z" fill="var(--ink-red)"/>
    </svg>

    <p class="script wish wish--line1">happy</p>
    <p class="script wish wish--line2">life</p>

    <p class="wedding-date">22.7.2018</p>
  </section>
</div>
</body>
</html>
```